Redesign start page for existing online shop

We are selling building material (chimneys and flue pipes) as well as fireplaces (stoves). For this online shop we need a new start page. The domain is kaminwelt-versand.de. Here you can see the current design. We want a smoother design with just one banner in the middle instead of the three in the first row. The look has to be more professional and trustworthy. You can therefore play with the colors. We want to try some different orange instead of our yellow / orange color. A few more things: - The phone number has to be bigger and more highlighted - So the 5 advantages at the top should be shown in a different way - New design for the products below - New footer

Target Market(s)

Germany and other countries in Europe.

Industry/Entity Type

Home Builder

Number of Pages Required

1 page

Font styles to use
Other font styles liked:
• Please se the font on our current site.

Colors
f78f20
f68d4c

Requirements
Must have
• - Clear design - Trustworthy look - All elements Which are now shown shoulderstand be still there after redesigning -
Nice to have
• - See the Following sites to have a clou about our wishes: glutvia.de warmbrio.de

```html
<!DOCTYPE html>
<html lang="de">
<head>
<meta charset="utf-8">
<title>Kaminwelt Versand – Startseite</title>
<link href="https://fonts.googleapis.com/css2?family=Open+Sans:wght@400;600;700;800&display=swap" rel="stylesheet">
<style>
:root{
  --orange:#f78f20;
  --orange-soft:#f68d4c;
  --red:#e8452c;
  --ink:#222;
  --text:#444;
  --muted:#777;
  --light:#f1f1f1;
  --line:#ddd;
  --dark:#464646;
  --darker:#262626;
  --darkest:#1b1b1b;
  --white:#fff;
}
*{box-sizing:border-box;margin:0;padding:0}
html,body{width:1200px;height:3448px;overflow:hidden}
body{font-family:"Open Sans",Arial,sans-serif;color:var(--text);background:var(--white)}
a{color:inherit;text-decoration:none}
.wrap{width:1040px;margin:0 auto;position:relative}

.topbar{height:37px;background:#f4f4f4;border-bottom:1px solid #e4e4e4;font-size:12px;color:#333}
.topbar .wrap{display:flex;justify-content:space-between;align-items:center;height:37px;padding:0 40px;width:1200px}
.usp{display:flex;gap:28px}
.usp span::before{content:"";display:inline-block;width:10px;height:10px;border:2px solid var(--orange);border-radius:50%;margin-right:7px;vertical-align:-1px}
.toplinks{display:flex;gap:10px}
.toplinks a+a::before{content:"|";margin-right:10px;color:#aaa}

.header{height:119px;background:linear-gradient(#fff,#f2f2f2)}
.header .wrap{display:flex;justify-content:space-between;align-items:center;height:119px;width:1120px}
.brand{display:flex;align-items:center;gap:14px}
.brand-mark{width:50px;height:50px;border-radius:50%;border:4px solid var(--orange)}
.brand-name{font-size:30px;font-weight:600;line-height:32px;color:#333;letter-spacing:.5px}
.contact{display:flex;align-items:center;gap:12px}
.seal{width:54px;height:54px;border-radius:50%;background:#2b2b2b;border:3px solid var(--orange)}
.phone{font-size:24px;font-weight:700;color:var(--red)}
.phone small{display:block;font-size:12px;font-weight:400;color:#333}
.phone svg{vertical-align:-3px;margin-right:4px}

.nav{position:absolute;top:156px;left:138px;width:925px;height:50px;background:#fff;border-radius:4px;box-shadow:0 3px 8px rgba(0,0,0,.25);display:flex;z-index:2}
.nav a{flex:1;display:flex;align-items:center;justify-content:center;gap:10px;font-size:16px;font-weight:600;color:#333;border-right:1px solid var(--line)}
.nav a:last-child{border:0}
.nav a.active{color:var(--red)}
.nav a i{width:8px;height:8px;border-right:2.5px solid #333;border-bottom:2.5px solid #333;transform:rotate(45deg);margin-top:-5px}

.hero{position:relative;height:602px;background:linear-gradient(160deg,#6f7a62 0%,#5b5a55 35%,#7b7875 60%,#55514e 100%)}
.hero-text{position:absolute;right:30px;bottom:30px;text-align:center;color:#fff;font-size:38px;line-height:42px;text-shadow:0 1px 3px rgba(0,0,0,.6)}
.hero .arrow{position:absolute;top:280px;width:34px;height:34px;border-radius:50%;background:rgba(0,0,0,.55)}
.hero .arrow::after{content:"";position:absolute;top:12px;width:9px;height:9px;border-left:3px solid #fff;border-bottom:3px solid #fff}
.arrow.prev{left:22px}.arrow.prev::after{left:13px;transform:rotate(45deg)}
.arrow.next{right:22px}.arrow.next::after{left:9px;transform:rotate(-135deg)}

.clients{height:116px;background:#f0f0f0;border-bottom:1px solid #e0e0e0}
.clients .wrap{display:flex;align-items:center;height:116px;width:1120px;gap:22px}
.clients h2{font-size:34px;font-weight:400;line-height:36px;color:#222;width:140px}
.clients h2 span{color:var(--red)}
.clients .chev{width:12px;height:12px;border-left:2px solid #bbb;border-bottom:2px solid #bbb;transform:rotate(45deg)}
.clients .chev.r{transform:rotate(-135deg)}
.client{width:142px;height:62px;background:#fff;border:1px solid #ddd;display:flex;align-items:center;justify-content:center;font-size:14px;font-weight:700;color:#333}

.features{height:409px}
.features .wrap{display:flex;justify-content:space-between;padding-top:50px;width:1000px}
.feature{width:196px;text-align:center}
.ring{width:126px;height:126px;margin:0 auto 20px;border-radius:50%;border:6px solid var(--orange);display:flex;align-items:center;justify-content:center;background:#fff;box-shadow:0 0 0 4px #fde7cf}
.ring.red{border-color:var(--red);box-shadow:0 0 0 4px #fbd9d2}
.feature h3{font-size:14px;font-weight:700;color:#222;line-height:18px;white-space:nowrap}
.feature p{font-size:12.5px;line-height:17px;margin-top:5px;height:52px;overflow:hidden}
.more{position:relative;height:22px;margin-top:12px}
.more::before{content:"";position:absolute;left:0;right:0;top:10px;border-top:1px solid var(--orange)}
.more b{position:absolute;left:50%;top:0;margin-left:-11px;width:22px;height:22px;border-radius:50%;background:var(--orange);color:#fff;font-size:16px;line-height:21px}
.feature.red .more::before{border-color:var(--red)}.feature.red .more b{background:var(--red)}

.steps{height:575px;background:var(--light);text-align:center}
.steps h2{padding-top:50px;font-size:40px;font-weight:400;color:#222}
.steps h2 span{color:var(--red)}
.steps .sub{font-size:15px;margin-top:22px;color:#333}
.step-row{display:flex;justify-content:space-between;width:980px;margin:40px auto 0}
.step{width:230px}
.step .ring{width:150px;height:150px;background:#fff;border-width:6px}
.step p{font-size:16px;line-height:22px;color:#222;white-space:nowrap}
.cta{margin-top:44px;display:flex;justify-content:center;align-items:center;gap:24px;font-size:18px;font-weight:700;color:#222}
.btn{display:inline-flex;align-items:center;gap:8px;background:var(--orange);color:#222;font-size:14px;font-weight:700;border-radius:18px;height:38px;padding:0 16px 0 6px}
.btn .dot{width:28px;height:28px;border-radius:50%;background:#fff;border:2px solid var(--orange-soft)}

.products{height:598px}
.products .wrap{display:flex;justify-content:space-between;padding-top:70px;width:1045px}
.product{width:246px;text-align:center}
.product .photo{height:265px;background:linear-gradient(#f7f7f7,#d9d9d9);border:1px solid #ddd}
.price{height:36px;background:#2a2a2a;color:#fff;font-size:17px;line-height:36px}
.product h3{font-size:16px;font-weight:700;color:#222;margin-top:24px}
.product p{font-size:13px;line-height:18px;margin-top:10px;height:72px}
.product .btn{height:34px;font-size:12px;margin-top:20px}
.product .btn .dot{width:24px;height:24px}

.seo{height:451px;background:var(--dark);color:#e8e8e8}
.seo .wrap{padding-top:56px;width:1040px}
.seo h2{font-size:24px;font-weight:400;color:var(--orange);line-height:34px}
.seo p{font-size:13px;line-height:21px;margin-top:28px;color:#ddd}
.seo .btn{margin:36px auto 0;display:flex;width:160px}

.newsletter{height:115px;background:var(--orange)}
.newsletter .wrap{display:flex;align-items:center;height:115px;width:1040px;gap:18px}
.newsletter .mail{width:54px;height:54px;border-radius:50%;background:#2a2a2a;display:flex;align-items:center;justify-content:center}
.newsletter h2{font-size:28px;font-weight:400;color:#222;width:350px}
.newsletter .field{width:380px;height:42px;background:#fff;border:1px solid #e5a45c;font-size:13px;color:#999;line-height:40px;padding:0 12px;margin-left:20px}
.newsletter .submit{margin-left:auto;width:196px;height:42px;background:#2a2a2a;color:#fff;font-size:17px;font-weight:700;line-height:42px;text-align:center}

.footer{height:345px;background:var(--darker);color:#ccc;font-size:12px}
.footer .wrap{display:flex;padding-top:56px;width:1040px;gap:40px}
.footer h3{font-size:18px;font-weight:400;color:#fff;padding-bottom:14px;border-bottom:1px solid #444;margin-bottom:22px}
.links{width:280px}
.links ul{list-style:none;columns:2;line-height:36px}
.links li{white-space:nowrap}
.links li::before{content:"› ";color:#999}
.links li.on{color:var(--orange)}
.kontakt{width:480px;display:flex;flex-wrap:wrap;font-size:11.5px}
.kontakt h3{width:100%}
.kontakt .col{width:265px;line-height:19px}
.kontakt .col+.col{width:215px}
.kontakt .col p{display:flex;gap:10px;margin-bottom:24px;white-space:nowrap}
.kontakt b{color:#fff}
.kontakt svg{flex:none;margin-top:2px}
.map{width:200px}
.map .disc{width:200px;height:200px;border-radius:50%;background:radial-gradient(circle at 55% 45%,#f3efe6,#d9d6cc);border:5px solid #eee}

.bottom{height:53px;background:var(--darkest)}
.bottom .wrap{display:flex;justify-content:space-between;align-items:center;height:53px;width:1040px;color:#ccc;font-size:12px}
.social{display:flex;gap:8px}
.social span{width:34px;height:34px;border-radius:50%;background:#fff}
</style>
</head>
<body>

<div class="topbar"><div class="wrap">
  <div class="usp"><span>In 5 min zum Angebot</span><span>führende Marken</span><span>Mit uns Förderung erhalten</span></div>
  <div class="toplinks"><a href="#">Standorte</a><a href="#">für Händler</a><a href="#">Installateure</a></div>
</div></div>

<header class="header"><div class="wrap">
  <div class="brand"><span class="brand-mark"></span><span class="brand-name">KAMINWELT<br>VERSAND</span></div>
  <div class="contact">
    <span class="seal" aria-label="Gütesiegel"></span>
    <div class="phone"><svg width="20" height="20" viewBox="0 0 24 24"><path fill="#e8452c" d="M6.6 10.8a15 15 0 006.6 6.6l2.2-2.2a1 1 0 011-.25 11.4 11.4 0 003.6.57 1 1 0 011 1V20a1 1 0 01-1 1A17 17 0 013 4a1 1 0 011-1h3.5a1 1 0 011 1 11.4 11.4 0 00.57 3.6 1 1 0 01-.25 1z"/></svg>0800 7 310 510<small>Mo - Fr: 9-20 Uhr &nbsp;|&nbsp; Sa: 11-17 Uhr</small></div>
  </div>
</div></header>

<nav class="nav">
  <a class="active" href="#">Home</a>
  <a href="#">Online-Shop <i></i></a>
  <a href="#">Services <i></i></a>
  <a href="#">Jobs</a>
  <a href="#">Kontakt</a>
</nav>

<section class="hero" role="img" aria-label="Foto: Edelstahlschornstein auf einem Ziegeldach">
  <span class="arrow prev"></span><span class="arrow next"></span>
  <p class="hero-text">We are selling building material<br>(chimneys and flue pipes) as well as fire places (stoves).</p>
</section>

<section class="clients"><div class="wrap">
  <h2><span>Unsere</span><br>Kunden</h2>
  <span class="chev"></span>
  <div class="client">Nordtherm</div>
  <div class="client">RauchPro</div>
  <div class="client">Ofenkraft</div>
  <div class="client">Zugwerk</div>
  <div class="client">Kaminbau Süd</div>
  <span class="chev r"></span>
</div></section>

<section class="features"><div class="wrap">
  <div class="feature red">
    <div class="ring red"><svg width="54" height="54" viewBox="0 0 54 54" fill="none" stroke="#222" stroke-width="3"><rect x="10" y="6" width="30" height="40" rx="2"/><path d="M16 16h18M16 24h18M16 32h10"/><path d="M34 40l12-16 4 3-12 16-5 1z"/></svg></div>
    <h3>Verbindliches Heizungs<br>Angebot sofort!</h3>
    <p>Geben Sie nur wenige Eckdaten zu Ihrem Haus in unseren Konfigurator ein.</p>
    <div class="more"><b>+</b></div>
  </div>
  <div class="feature">
    <div class="ring"><svg width="54" height="54" viewBox="0 0 54 54" fill="none" stroke="#222" stroke-width="3.5"><path d="M12 42l20-20M34 12a8 8 0 00-2 10l6 6a8 8 0 0010-2l-5-1-2-5z"/><path d="M12 12l30 30M10 10l6-2 2 6"/></svg></div>
    <h3>Mehr als 30 Jahre<br>Meisterqualität!</h3>
    <p>Erfahrung und Kompetenz sind der Garant für einen hervorragenden Service.</p>
    <div class="more"><b>+</b></div>
  </div>
  <div class="feature">
    <div class="ring"><svg width="54" height="54" viewBox="0 0 54 54" fill="none" stroke="#222" stroke-width="3"><rect x="8" y="8" width="24" height="36"/><path d="M14 16h12M14 24h12"/><rect x="32" y="26" width="14" height="18"/><path d="M36 32h6"/></svg></div>
    <h3>Neue Heizung bereits<br>ab 39 € im Monat!</h3>
    <p>Eine neue, umweltfreundliche und energiesparende Heizung liefern und installieren wir.</p>
    <div class="more"><b>+</b></div>
  </div>
  <div class="feature">
    <div class="ring"><svg width="54" height="54" viewBox="0 0 54 54" fill="none" stroke="#222" stroke-width="3"><circle cx="27" cy="27" r="19"/><path d="M27 38c-6 0-8-5-6-9 1 3 3 3 3 3-1-6 3-10 6-12 0 4 5 6 5 11 0 4-3 7-8 7z"/></svg></div>
    <h3>10 Jahre Garantie auf<br>Ihre neue Heizung!</h3>
    <p>Wir verbauen Qualität und bieten Ihnen daher ab sofort auf alle von uns eingebauten Anlagen Garantie.</p>
    <div class="more"><b>+</b></div>
  </div>
</div></section>

<section class="steps">
  <h2><span>So</span> funktioniert's</h2>
  <p class="sub">In wenigen Schritten zum richtigen Angebot für Ihre Sanierung</p>
  <div class="step-row">
    <div class="step"><div class="ring"><svg width="60" height="60" viewBox="0 0 60 60" fill="none" stroke="#222" stroke-width="3"><rect x="8" y="10" width="44" height="32" rx="2"/><path d="M22 50h16M30 42v8M16 20h28M16 28h20"/></svg></div><p>Daten online<br>eingeben</p></div>
    <div class="step"><div class="ring"><svg width="60" height="60" viewBox="0 0 60 60" fill="none" stroke="#222" stroke-width="3"><path d="M8 30L30 12l22 18M14 26v22h32V26"/><rect x="24" y="34" width="12" height="14"/></svg></div><p>Aufmaß und Beratung<br>durch Kundenberater</p></div>
    <div class="step"><div class="ring"><svg width="60" height="60" viewBox="0 0 60 60" fill="none" stroke="#222" stroke-width="3"><rect x="12" y="8" width="30" height="42" rx="2"/><path d="M18 18h18M18 26h18M18 34h10"/><path d="M38 44l12-16 4 3-12 16-5 1z"/></svg></div><p>Angebot von 2 flammwerk<br>Handwerkern</p></div>
    <div class="step"><div class="ring"><svg width="60" height="60" viewBox="0 0 60 60" fill="none" stroke="#222" stroke-width="3"><path d="M6 22h30v20H6zM36 28h10l6 8v6H36z"/><circle cx="16" cy="44" r="4"/><circle cx="44" cy="44" r="4"/></svg></div><p>Ausführung</p></div>
  </div>
  <div class="cta">Jetzt unverbindlich eine Anfrage stellen! <a class="btn" href="#"><span class="dot"></span>Anfrage stellen »</a></div>
</section>

<section class="products"><div class="wrap">
  <article class="product">
    <div class="photo" role="img" aria-label="Produktfoto: Schornsteinverlängerung aus Edelstahl"></div>
    <div class="price">ad € 63,00</div>
    <h3>Schornsteinverlängerung</h3>
    <p>Kaminverlängerungen frei konfigurierbar nach Ihren Wunschmaßen und in Flandarbeit nach höchsten Ansprüchen hergestellt.</p>
    <a class="btn" href="#"><span class="dot"></span>JETZT ANSEHEN</a>
  </article>
  <article class="product">
    <div class="photo" role="img" aria-label="Produktfoto: Schornsteinabdeckung"></div>
    <div class="price">ad € 116,50</div>
    <h3>Schornsteinabdeckung</h3>
    <p>Kaminabdeckungen für alle Schornsteine individuell bestellen. Für Langlebigkeit und Qualität für Ihren Schornstein.</p>
    <a class="btn" href="#"><span class="dot"></span>JETZT ANSEHEN</a>
  </article>
  <article class="product">
    <div class="photo" role="img" aria-label="Produktfoto: Wanddurchführung"></div>
    <div class="price">ad € 99,90</div>
    <h3>Wanddurchführung</h3>
    <p>Kaminverlängerungen frei konfigurierbar nach Ihren Wunschmaßen und in Flandarbeit nach höchsten Ansprüchen hergestellt.</p>
    <a class="btn" href="#"><span class="dot"></span>JETZT ANSEHEN</a>
  </article>
  <article class="product">
    <div class="photo" role="img" aria-label="Produktfoto: schwarzes Ofenrohr"></div>
    <div class="price">ad € 9,99</div>
    <h3>Ofenrohr</h3>
    <p>Ofenrohre in den Farben schwarz oder gussgrau in Premiumqualität direkt hier bestellen. Höchste Qualität für Ihre Sicherheit.</p>
    <a class="btn" href="#"><span class="dot"></span>JETZT ANSEHEN</a>
  </article>
</div></section>

<section class="seo"><div class="wrap">
  <h2>Edelstahlschornsteine, Schornsteinverlängerungen, Ofenrohre und Schornstein Zubehör – alles bei kaminwelt-versand.de günstig kaufen.</h2>
  <p>Kann ich einen Edelstahlschornstein im Internet kaufen? Diese Frage haben Sie sich bestimmt noch nie gestellt. Bei anderen Waren ist das eine Selbstverständlichkeit, aber bei einem Edelstahlkamin denkt man zunächst nicht ans Onlineshopping. Dabei gibt es schon seit einigen Jahren diverse Plattformen die alles rund um das Thema Edelstahlschornstein anbieten. Allerdings betreiben diese Anbieter ihre Webshops nur nebenher. Dies spiegelt sich in der schlechten Benutzerfreundlichkeit und der teilweise stark veralteten Technik der Seiten wider. Kaminwelt-Versand ist hier einen neuen Weg gegangen. Das Ziel war es, einen Onlineshop für Edelstahlschornsteine und Schornstein Zubehör auf die Beine zu stellen, der nicht nur professionell und nach dem neuesten Stand der Technik aufgebaut ist, sondern Ihnen auch die Sicherheit und Usability bietet, die Sie von großen Onlineplattformen anderer Branchen gewohnt sind. Mit einer effizienten Organisation, modernster Technik und jahrelanger Erfahrung mit dem Produkt Edelstahlschornstein, konnte dieser Anspruch erfüllt werden. Beste Usability, geprüfter Datenschutz, hochwertige Waren und eine kompetente telefonische Beratung runden Ihr Einkaufserlebnis bei kaminwelt-versand.de ab.</p>
  <a class="btn" href="#"><span class="dot"></span>Weiterlesen</a>
</div></section>

<section class="newsletter"><div class="wrap">
  <span class="mail"><svg width="28" height="20" viewBox="0 0 28 20" fill="none" stroke="#fff" stroke-width="2.5"><rect x="1" y="1" width="26" height="18"/><path d="M1 1l13 10L27 1"/></svg></span>
  <h2>Anmeldung für Newsletter</h2>
  <div class="field">Gib deine E-Mail hier ein</div>
  <a class="submit" href="#">ABONNIEREN</a>
</div></section>

<footer class="footer"><div class="wrap">
  <div class="links">
    <h3>Nützliche Links</h3>
    <ul><li class="on">Häufige Fragen</li><li>AGB</li><li>Lieferung &amp; Zahlung</li><li>Impressum</li><li>Blog</li><li>Über uns</li><li>Widerruf</li><li>Datenschutz</li><li>Kontaktieren Sie uns</li><li>Glossar</li></ul>
  </div>
  <div class="kontakt">
    <h3>Kontaktiere uns</h3>
    <div class="col">
      <p><svg width="12" height="16" viewBox="0 0 12 16"><path fill="#fff" d="M6 0a6 6 0 016 6c0 4-6 10-6 10S0 10 0 6a6 6 0 016-6zm0 4a2 2 0 100 4 2 2 0 000-4z"/></svg><b>Lindenhofweg 7<br>80335 München<br>Deutschland</b></p>
      <p><b>Kaminwelt-Versand<br>Durchschnittliche Bewertung: 4,71 (von 5).<br>Ermittelt aus 265 Bewertungen.</b></p>
    </div>
    <div class="col">
      <p><b>Kostenlose Beratung</b></p>
      <p><svg width="14" height="14" viewBox="0 0 24 24"><path fill="#fff" d="M6.6 10.8a15 15 0 006.6 6.6l2.2-2.2a1 1 0 011-.25 11.4 11.4 0 003.6.57 1 1 0 011 1V20a1 1 0 01-1 1A17 17 0 013 4a1 1 0 011-1h3.5a1 1 0 011 1 11.4 11.4 0 00.57 3.6 1 1 0 01-.25 1z"/></svg>08131 / 402 118 0</p>
      <p><svg width="14" height="14" viewBox="0 0 14 14" fill="none" stroke="#fff" stroke-width="1.6"><circle cx="7" cy="7" r="6"/><path d="M7 3v4h3"/></svg>Mo. - Fr. von 09:00 bis 18:00 Uhr</p>
      <p><svg width="14" height="12" viewBox="0 0 14 12" fill="none" stroke="#fff" stroke-width="1.6"><rect x="1" y="1" width="12" height="10"/><path d="M1 1l6 5 6-5"/></svg>info@kaminwelt-versand.de</p>
    </div>
  </div>
  <div class="map">
    <h3>Landkarte</h3>
    <div class="disc" role="img" aria-label="Stadtplanausschnitt mit Firmenstandort in München"></div>
  </div>
</div></footer>

<div class="bottom"><div class="wrap">
  <span>Copyright © 2016 Kaminwelt Versand. All Rights Reserved.</span>
  <div class="social" aria-label="Soziale Netzwerke"><span></span><span></span><span></span><span></span><span></span></div>
</div></div>

</body>
</html>
```